CAPPUCCINO ART FOR VELLOR BOX PACKAGING DESIGN

The product is UHT Milk in Vellor Box pagkaging.
Flavour: Mocha

The measurement is around:
- (Front & Back): 4.8 cm (Width) x 12 cm (Height)
- (Sides): 3.8 cm (Width) x 12 cm (Height)
Real measurement attached

Temporary Brand name: DUNRA.
However, you can also propose a brand name to match your design

I want the product design to have a cappuccino art.
The shape/ art could be anything: leafs, animal picture, or other artistic forms.
The possibility is endless.
Please refer to the examples attached.

Other than the main focus of the cappuccino art, your can add other elements to make it more appealing and tempting, such as the cappuccino cup, plate, coffee beans, biscuits, etc. Basically these added elements are to give the "Real Feel" of tasting a cappuccino (in this case is mocha flavor) drink.

Create something different. Something extraordinary.

All the best and Good Luck!

Best Regards,
Marcus
+65 9143 6072
Updates

Project Deadline Extended Reason: I HAVE NOT FOUND ANY GOOD DESIGNS THAT IS CLOSE TO MY EXPECTATION.PLEASE DO YOUR BEST TO SUBMIT BETTER DESIGN QUALITY.THANK YOU AND GOOD LUCK!REGARDS,MARCUS Added Monday, March 9, 2015

Project Deadline Extended Reason: I haven't found good designs yet.Please submit more designs with much better quality.Best Regards,Marcus Added Wednesday, April 8, 2015

Project Deadline Extended Reason: I WOULD LIKE TO RECEIVE MUCH BETTER DESIGNS. Added Friday, June 26, 2015

Dear All Designers, I have extended the project deadline as I haven't found a satisfactory design yet. I have also updated the project brief, and narrowed the concept to make a cappuccino art as the main object on my product label. I believe with the provision of this concept, you should be able to create a great design. Thank you, Marcus +65 9143 6072

Industry/Entity Type

Product

Requirements
Must have
• I want the product design to have a cappuccino art.
• The shape/ art could be anything: leafs, animal picture, or other artistic forms.
• The possibility is endless.
• Please refer to the examples attached.

```html
<!DOCTYPE html>
<html lang="en">
<head>
<meta charset="utf-8">
<title>DUNRA Mocha Milk Packaging</title>
<link rel="stylesheet" href="https://fonts.googleapis.com/css2?family=Quicksand:wght@400;500&family=Pacifico&family=Archivo+Narrow:wght@400;700&display=swap">
<style>
  :root {
    --navy: #0f2a3d;
    --leaf: #9edc4e;
    --blush: #f5e9e6;
    --rose: #f08a8f;
    --cream: #f0e6c0;
    --stage: #808080;
  }
  * { box-sizing: border-box; margin: 0; padding: 0; }
  html, body { width: 1200px; height: 1000px; overflow: hidden; }
  body { position: relative; background: var(--stage); font-family: "Quicksand", sans-serif; color: var(--navy); }

  .brand-panel { position: absolute; left: 800px; width: 400px; height: 500px; display: flex; align-items: center; justify-content: center; }
  .brand-panel--light { top: 0; background: var(--cream); }
  .brand-panel--dark { top: 500px; background: var(--navy); }
  .brand-name { font-family: "Quicksand", sans-serif; font-weight: 500; letter-spacing: 2px; line-height: 1; }
  .brand-panel .brand-name { font-size: 78px; padding-top: 60px; }
  .brand-panel--light .brand-name { color: var(--navy); }
  .brand-panel--dark .brand-name { color: var(--leaf); padding-top: 40px; }

  .label { position: absolute; top: 95px; height: 810px; box-shadow: 3px 4px 6px rgba(0,0,0,.35); background: var(--leaf); }
  .label--front { left: 76px; width: 324px; }
  .label--back { left: 467px; width: 257px; top: 97px; height: 808px; }
  .band { position: absolute; left: 0; right: 0; }
  .band--navy { top: 0; background: var(--navy); }
  .band--blush { background: var(--blush); }
  .label--front .band--navy { height: 218px; }
  .label--front .band--blush { top: 218px; height: 162px; }
  .label--back .band--navy { height: 216px; }
  .label--back .band--blush { top: 216px; height: 164px; }

  .abs { position: absolute; left: 0; right: 0; text-align: center; }
  .label--front .brand-name { top: 102px; font-size: 60px; color: var(--leaf); }
  .label--back .brand-name { top: 112px; font-size: 44px; color: var(--rose); }

  .script { font-family: "Pacifico", cursive; line-height: 1; }
  .tag-fresh { top: 182px; font-size: 28px; color: var(--rose); }
  .product-name { top: 232px; font-size: 96px; color: var(--navy); }
  .flavour { top: 398px; font-size: 38px; color: var(--navy); }
  .flavour-note { top: 447px; font-size: 18px; }
  .mascot { position: absolute; left: 76px; top: 483px; width: 172px; height: 208px; border-radius: 40% 40% 30% 30%; background: radial-gradient(circle at 50% 55%, #f5ecec 0 45%, var(--rose) 46% 55%, #f5ecec 56%); }
  .source-label { top: 699px; font-size: 14px; }
  .nutrients { top: 717px; font-size: 18.5px; line-height: 23px; }
  .volume { font-size: 18px; }
  .label--front .volume { top: 773px; }
  .label--back .volume { top: 772px; }

  .blurb { top: 232px; left: 38px; right: 38px; font-size: 11.5px; line-height: 14.6px; }

  .nutrition { position: absolute; left: 30px; top: 403px; width: 196px; height: 340px; border: 2px solid var(--navy); padding: 2px 5px; font-family: "Archivo Narrow", sans-serif; font-size: 10.5px; line-height: 1.2; }
  .nutrition h2 { font-family: "Archivo Narrow", sans-serif; font-weight: 700; font-size: 21px; line-height: 1; letter-spacing: .3px; display: flex; justify-content: space-between; }
  .nutrition .serving { font-size: 10px; border-bottom: 4px solid var(--navy); padding-bottom: 6px; }
  .nutrition .small { font-size: 8px; font-weight: 700; padding-top: 8px; }
  .row { display: flex; justify-content: space-between; border-top: 1px solid rgba(15,42,61,.35); padding: 3px 0; }
  .row b { font-weight: 700; }
  .row.indent { padding-left: 13px; }
  .row.thick { border-top: 4px solid var(--navy); }
  .row.right { justify-content: flex-end; font-size: 8px; font-weight: 700; }
  .footnote { font-size: 7.5px; border-top: 1px solid rgba(15,42,61,.35); padding-top: 3px; }
</style>
</head>
<body>
  <section class="label label--front">
    <div class="band band--navy"></div>
    <div class="band band--blush"></div>
    <div class="abs brand-name">DUNRA</div>
    <div class="abs script tag-fresh">fresh</div>
    <div class="abs script product-name">Milk</div>
    <div class="abs script flavour">mocha</div>
    <div class="abs flavour-note">flavoured</div>
    <div class="mascot" role="img" aria-label="Cartoon cow mascot illustration"></div>
    <div class="abs source-label">Source of</div>
    <div class="abs nutrients">Vitamin A, D3, B1, B2, B6, B12<br>Calcium and Phosphor</div>
    <div class="abs volume">1 LITRE</div>
  </section>

  <section class="label label--back">
    <div class="band band--navy"></div>
    <div class="band band--blush"></div>
    <div class="abs brand-name">DUNRA</div>
    <p class="abs blurb">Lorem ipsum dolor sit amet, consectetuer adipiscing elit, sed diam nonummy nibh euismod tincidunt ut laoreet dolore magna aliquam erat volutpat. Ut wisi enim ad minim veniam, quis nostrud exerci tation ullamcorper suscipit lobortis nisl ut aliquip ex ea commodo consequat.</p>
    <div class="nutrition">
      <h2><span>Nutrition</span><span>Facts</span></h2>
      <div class="serving">Serving Size 1 cup (228g)<br>Servings Per Container 2</div>
      <div class="small">Amount Per Serving</div>
      <div class="row"><span><b>Calories</b> 260</span><span>Calories from Fat 120</span></div>
      <div class="row right">% Daily Value*</div>
      <div class="row"><span><b>Total Fat</b> 13g</span><b>20%</b></div>
      <div class="row indent"><span>Saturated Fat 5g</span><b>25%</b></div>
      <div class="row indent"><span>Trans Fat 2g</span><span></span></div>
      <div class="row"><span><b>Cholesterol</b> 30mg</span><b>10%</b></div>
      <div class="row"><span><b>Sodium</b> 660mg</span><b>28%</b></div>
      <div class="row"><span><b>Total Carbohydrate</b> 31g</span><b>10%</b></div>
      <div class="row indent"><span>Dietary Fiber 0g</span><b>0%</b></div>
      <div class="row indent"><span>Sugars 5g</span><span></span></div>
      <div class="row"><span><b>Protein</b> 5g</span><span></span></div>
      <div class="row thick"><span>Vitamin A 4% &nbsp;&nbsp;&nbsp;&nbsp;•</span><span>Vitamin C 2%</span></div>
      <div class="row"><span>Calcium 15% &nbsp;&nbsp;&nbsp;&nbsp;•</span><span>Iron 4%</span></div>
      <div class="footnote">*Percent Daily Values are based on a 2,000 calorie diet.</div>
    </div>
    <div class="abs volume">1 LITRE</div>
  </section>

  <section class="brand-panel brand-panel--light"><span class="brand-name">DUNRA</span></section>
  <section class="brand-panel brand-panel--dark"><span class="brand-name">DUNRA</span></section>
</body>
</html>
```